Postcard Design

Law office.
Details are on the attached pdf file:
NOTE: the following items are to be changed, as follows:
1. price is 799
2. delete "Expires 2-8-13"
3. make "Nevada County's..." into "Northern California's ... "
4. Someplace where it fits nicely, add "Fast, Easy, Done!"
5. Delete "no obligation first visit"
6. That attached pdf was a successful ad so I want to maintain that look GENERALLY, but I'm not stuck on anything in particular. Some freedom to play with it for a perfect ad.
7. I'll attach the revised picture and the logo.

```html
<!DOCTYPE html>
<html lang="en">
<head>
<meta charset="UTF-8">
<title>Law Office Of Daniel R. Moreno – Estate Plans Postcard</title>
<link href="https://fonts.googleapis.com/css2?family=Marcellus&family=Libre+Baskerville:ital@0;1&family=Oswald:wght@500;700&display=swap" rel="stylesheet">
<style>
  :root {
    --ink: #0b0b0b;
    --sky-light: #f4fafd;
    --sky-mid: #d6edf8;
    --sky-deep: #b6dcf1;
    --photo-top: #8a8f95;
    --photo-bottom: #2c2f33;
    --frame: #ffffff;
  }
  * { margin: 0; padding: 0; box-sizing: border-box; }
  html, body { width: 1200px; height: 800px; overflow: hidden; background: #ffffff; }
  .postcard {
    position: relative;
    width: 1200px;
    height: 800px;
    overflow: hidden;
    color: var(--ink);
    background: radial-gradient(ellipse at 15% 10%, var(--sky-light) 0%, var(--sky-mid) 55%, var(--sky-deep) 100%);
  }
  .postcard > * { position: absolute; }

  .headline {
    top: 18px; left: 0; width: 1200px;
    text-align: center;
    font-family: "Marcellus", serif;
    font-size: 49px;
    letter-spacing: 0.5px;
  }
  .subhead {
    top: 80px; left: 0; width: 1200px;
    text-align: center;
    font-family: "Libre Baskerville", serif;
    font-style: italic;
    font-size: 29px;
  }
  .price {
    top: 118px; left: 302px;
    font-family: "Libre Baskerville", serif;
    font-size: 150px;
    line-height: 1;
    letter-spacing: -6px;
  }
  .price-dollar { font-size: 96px; vertical-align: 6px; letter-spacing: 0; }
  .value {
    top: 174px; left: 646px;
    font-family: "Oswald", sans-serif;
    font-weight: 500;
    font-size: 38px;
    line-height: 1;
  }
  .expiry {
    top: 218px; left: 646px;
    font-family: "Oswald", sans-serif;
    font-weight: 500;
    font-size: 19px;
  }
  .tagline {
    top: 298px; left: 0; width: 1200px;
    text-align: center;
    font-family: "Marcellus", serif;
    font-size: 45px;
  }
  .tagline-sub {
    top: 350px; left: 0; width: 1200px;
    text-align: center;
    font-family: "Libre Baskerville", serif;
    font-size: 17px;
  }
  .portrait {
    top: 380px; left: 40px;
    width: 284px; height: 383px;
    border: 6px solid var(--frame);
    background: linear-gradient(180deg, var(--photo-top) 0%, #5c6066 55%, var(--photo-bottom) 100%);
  }
  .call {
    top: 412px; left: 362px;
    font-family: "Oswald", sans-serif;
    font-weight: 500;
    font-size: 42px;
    line-height: 1;
  }
  .phone {
    top: 398px; left: 730px;
    font-family: "Oswald", sans-serif;
    font-weight: 700;
    font-size: 70px;
    line-height: 1;
    letter-spacing: 1px;
  }
  .office-label {
    top: 568px; left: 488px;
    font-family: "Libre Baskerville", serif;
    font-size: 22px;
  }
  .office-name {
    top: 598px; left: 380px;
    font-family: "Libre Baskerville", serif;
    font-size: 50px;
    line-height: 1;
    white-space: nowrap;
  }
  .website {
    top: 684px; left: 349px;
    font-family: "Libre Baskerville", serif;
    font-size: 24px;
    white-space: nowrap;
  }
  .notary {
    top: 724px; left: 560px;
    font-family: "Libre Baskerville", serif;
    font-size: 18px;
  }
  .seal {
    top: 520px; left: 1037px;
    width: 126px; height: 156px;
  }
  .since {
    top: 688px; left: 1010px; width: 180px;
    text-align: center;
    font-family: "Libre Baskerville", serif;
    font-size: 17px;
    line-height: 1.45;
  }
</style>
</head>
<body>
  <main class="postcard">
    <h1 class="headline">Northern California's Best In Estate Plans</h1>
    <p class="subhead">Living Trusts, Wills &amp; All Necessary Documents</p>

    <p class="price"><span class="price-dollar">$</span>799</p>
    <p class="value">OVER $2,000 VALUE</p>
    <p class="expiry">EXPIRES 2-8-13</p>

    <h2 class="tagline">PROTECT YOUR LOVED ONES!</h2>
    <p class="tagline-sub">FAST, EASY, DONE!</p>

    <div class="portrait" role="img" aria-label="Portrait photo of the attorney in a dark suit and tie"></div>

    <p class="call">IT'S EASY - CALL NOW!</p>
    <p class="phone">555-0142</p>

    <p class="office-label">Law Office Of</p>
    <p class="office-name">Daniel R. Moreno</p>
    <p class="website">Check me out at : www.DanielMorenoLaw.com</p>
    <p class="notary">Free Notarization</p>

    <svg class="seal" viewBox="0 0 126 156" aria-hidden="true">
      <rect x="3" y="3" width="120" height="150" fill="none" stroke="#0b0b0b" stroke-width="4"/>
    </svg>
    <p class="since">Thousands Served<br>Since 1998</p>
  </main>
</body>
</html>
```